Cheese Company Needs Product Label Design

Hello Designers. We are a cheese manufacturer and are looking for a label design for our new product "Fresh Mozzarella". The cheese balls come in a container that includes Sun-Dried Tomato with Parsley and Garlic marinated in oil.Here are the requirements:

1. LABEL: There will be a main circular label and a side label. The main circular label should be 3.83" in diameter. The side rectangular label should be 1.5" Length 3.25" Width.

2. DESIGN (LOGO): The company logo (attached) should be placed on the top in middle just like in the "product example" file that is included in the project.

3. DESIGN (PRODUCT NAME): The product name "FRESH MOZZARELLA" should be below the logo and be big in capital letters straight. Also include "ALL NATURAL" right above the name just like the "product example". Include "ORGANIC" icon somewhere on it.

4. DESIGN (PRODUCT DESCRIPTION): The product description "SUN-DRIED TOMATO and PARSLEY" should be below the product name. Make it look fancy.

5. DESIGN (PRODUCT PICTURE): I would like you to create a product drawing of many mozzarella balls with Sun-Dried Tomato and Parsley in it below the product description. Make sure it is attractive and pops-out on the label. Look at the "product example" to get an idea but please make sure you don't make it exactly the same. This is important as it needs to be arranged in such a way to not be too similar. Look at the file "inspiration 4" to see how it looks like.

6. DESIGN (BACKGROUND): The background of the picture should reflect a natural, organic, elegant scene. Think mountains, valleys, rivers flowing, nature, cows in the field and sun shining. I attached an "inspiration" photos here so you can get an idea. Make sure that the product is the main focus and not the background. It should be sophisticated with not too much color. Include a small border around the whole label.
DO NOT MAKE IT LOOK CARTOONISH!

7. WEIGHT: The weight of the product should be in the lower right corner and should say "NET WT. 12oz" and below that "(340g)".

8. KOSHER: The tablet kosher symbol should be on the lower right corner. Please look it up how it looks like.

9. SIDE LABEL: The side label should maintain the same color scheme as the main label similar to the "product example" attached here. It should have the Nutritional Facts attached, the Bar Code, and the "DISTRIBUTED BY: BRAVOLT LLC. 482 ELMCREST AVENUE, GLEN HARBOR, NY 11592". You can arrange it how you see fit but the Bar Code should be at least 1/3 of the label. Refer to the "product example" and keep close to its design. Put "MADE IN USA" on the right hand side. The last few things you need to do is put the Ingredients List below the Nutritional Facts as shown in the "product example", put the website "WWW.BRAVOLTFOODS.COM" below the Ingredients List, and put three social media icons going Facebook, Twitter, Instagram referring to @BravoltFoods somewhere near the bottom in it. Put the plant number on the side "PLANT NO. 52-7049" on it. Type out on the same side in bold letters to "KEEP REFRIGERATED".

10. FINAL: Thank you for accepting this project. As a main objective the label needs to look sophisticated and a high quality product. You can add your own twist on the design and keep it close to the rules. The Bar Code is not included in the files and will be given once we choose you as a designer for this. We also attached our "previous products" so you can get an idea of the type of company we are.

Target Market(s)

Cheese lovers, people who like snacks, natural food eaters.

Industry/Entity Type

Dairy Farm

Font styles to use
Serif
Script

Colors
ffffff
cadf82
f04a50
85cae6

Requirements
Must have
• All the point in the product description
Nice to have
• The points at a minimum.
Should not have
• Everything is explained. Do not make it look cartoonish!

```html
<!DOCTYPE html>
<html lang="en">
<head>
<meta charset="utf-8">
<title>Bravolt Fresh Mozzarella – Lid Label</title>
<link rel="stylesheet" href="https://fonts.googleapis.com/css2?family=Cinzel:wght@700;900&family=Pinyon+Script&display=swap">
<style>
  :root {
    --page: #ffffff;
    --ring-top: #ea4a50;
    --ring-bottom: #d2692c;
    --field-light: #f7ad98;
    --field-mid: #ea6a5e;
    --field-deep: #e24f4e;
    --band: #ffffff;
    --wine: #a51c2a;
    --wine-dark: #6e0c18;
    --cream: #fff8f0;
    --photo-cream: #f8e0d6;
    --photo-blush: #efa796;
    --photo-tomato: #d9534a;
    --photo-deep: #b8322f;
    --badge-red: #e8484c;
  }
  html, body {
    margin: 0;
    width: 1200px;
    height: 1200px;
    overflow: hidden;
    background: var(--page);
  }
  .label {
    display: block;
    width: 1200px;
    height: 1200px;
  }
  .brand-name {
    font-family: "Cinzel", serif;
    font-weight: 900;
    font-size: 74px;
    fill: var(--wine);
  }
  .product-title {
    font-family: "Cinzel", serif;
    font-weight: 900;
    fill: var(--wine);
    stroke: var(--cream);
    stroke-width: 3px;
    paint-order: stroke;
  }
  .product-title--fresh { font-size: 112px; }
  .product-title--mozz { font-size: 88px; }
  .flavour {
    font-family: "Pinyon Script", cursive;
    font-size: 62px;
    fill: var(--wine);
  }
  .claim, .weight {
    font-family: "Cinzel", serif;
    font-weight: 900;
    fill: var(--cream);
    stroke: var(--wine-dark);
    stroke-width: 3px;
    paint-order: stroke;
  }
  .claim { font-size: 46px; }
  .weight { font-size: 40px; }
</style>
</head>
<body>
<svg class="label" viewBox="0 0 1200 1200" xmlns="http://www.w3.org/2000/svg">
  <defs>
    <linearGradient id="ringGradient" x1="0" y1="0" x2="0" y2="1">
      <stop offset="0" stop-color="var(--ring-top)"/>
      <stop offset="1" stop-color="var(--ring-bottom)"/>
    </linearGradient>
    <radialGradient id="fieldGradient" cx="0.5" cy="0.62" r="0.7">
      <stop offset="0" stop-color="var(--field-light)"/>
      <stop offset="0.45" stop-color="var(--field-mid)"/>
      <stop offset="1" stop-color="var(--field-deep)"/>
    </radialGradient>
    <radialGradient id="photoGradient" cx="0.45" cy="0.4" r="0.75">
      <stop offset="0" stop-color="var(--photo-cream)"/>
      <stop offset="0.35" stop-color="var(--photo-blush)"/>
      <stop offset="0.75" stop-color="var(--photo-tomato)"/>
      <stop offset="1" stop-color="var(--photo-deep)"/>
    </radialGradient>
    <filter id="textShadow" x="-10%" y="-20%" width="120%" height="150%">
      <feDropShadow dx="2" dy="3" stdDeviation="2" flood-color="#5a0a12" flood-opacity="0.45"/>
    </filter>
    <clipPath id="discClip">
      <circle cx="600" cy="600" r="414"/>
    </clipPath>
  </defs>

  <!-- border rings -->
  <circle class="outer-ring" cx="600" cy="600" r="460" fill="url(#ringGradient)"/>
  <circle class="inner-ring" cx="600" cy="600" r="432" fill="var(--band)"/>

  <!-- inner disc -->
  <g class="disc" clip-path="url(#discClip)">
    <rect class="disc-field" x="180" y="180" width="840" height="444" fill="url(#fieldGradient)"/>
    <rect class="flavour-band" x="180" y="624" width="840" height="84" fill="var(--band)"/>
    <rect class="product-photo" x="204" y="708" width="796" height="320" fill="url(#photoGradient)"
          role="img" aria-label="Photo of sliced fresh mozzarella with halved tomatoes and basil leaves"/>
  </g>

  <!-- brand -->
  <text class="brand-name" x="600" y="340" text-anchor="middle" textLength="336" lengthAdjust="spacingAndGlyphs">BRAVOLT</text>

  <!-- product name -->
  <g filter="url(#textShadow)">
    <text class="product-title product-title--fresh" x="600" y="536" text-anchor="middle" textLength="356" lengthAdjust="spacingAndGlyphs">FRESH</text>
    <text class="product-title product-title--mozz" x="600" y="612" text-anchor="middle" textLength="600" lengthAdjust="spacingAndGlyphs">MOZZARELLA</text>
  </g>

  <!-- flavour -->
  <text class="flavour" x="600" y="684" text-anchor="middle" textLength="704" lengthAdjust="spacingAndGlyphs">Sun-Dried Tomato and Parsley</text>

  <!-- claim -->
  <text class="claim" x="604" y="772" text-anchor="middle" textLength="336" lengthAdjust="spacingAndGlyphs" filter="url(#textShadow)">All Natural</text>

  <!-- kosher mark -->
  <rect class="kosher-mark" x="920" y="744" width="22" height="24" rx="3" fill="rgba(255,248,240,0.35)" stroke="var(--cream)" stroke-width="2"/>

  <!-- organic certificate -->
  <g class="organic-badge">
    <circle cx="824" cy="840" r="64" fill="var(--cream)"/>
    <circle cx="824" cy="840" r="58" fill="none" stroke="var(--badge-red)" stroke-width="5"/>
    <circle cx="824" cy="840" r="40" fill="var(--badge-red)" opacity="0.18"/>
  </g>

  <!-- weight -->
  <g filter="url(#textShadow)">
    <text class="weight" x="601" y="952" text-anchor="middle" textLength="246" lengthAdjust="spacingAndGlyphs">Net Wt. 12oz</text>
    <text class="weight" x="600" y="992" text-anchor="middle" textLength="112" lengthAdjust="spacingAndGlyphs">(340g)</text>
  </g>
</svg>
</body>
</html>
```